Korvanta Business Card

Looking for business card ideas. Company name is Korvanta. Have a few basic ideas on attachment. Please submit anything with the logo and general information from attachment.

Industry/Entity Type

Business

```html
<!DOCTYPE html>
<html lang="en">
<head>
<meta charset="utf-8">
<title>Korvanta Business Card</title>
<link rel="stylesheet" href="https://fonts.googleapis.com/css2?family=Montserrat:wght@400;700&display=swap">
<style>
  :root {
    --brand-red: #ff0000;
    --ink: #111111;
    --paper: #ffffff;
    --frame: #d9d9d9;
  }
  * { margin: 0; padding: 0; box-sizing: border-box; }
  html, body {
    width: 1200px;
    height: 666px;
    overflow: hidden;
    background: var(--paper);
  }
  .canvas {
    position: relative;
    width: 1200px;
    height: 666px;
    background: var(--paper);
    font-family: "Montserrat", Arial, sans-serif;
    color: var(--ink);
  }
  .card {
    position: absolute;
    left: 88px;
    top: 62px;
    width: 1028px;
    height: 542px;
    border: 3px solid var(--frame);
    background: var(--paper);
  }
  .brand-band {
    position: absolute;
    left: 150px;
    top: 64px;
    width: 190px;
    height: 540px;
    background: var(--brand-red);
  }
  .band-circle {
    position: absolute;
    left: 145px;
    top: 255px;
    width: 210px;
    height: 210px;
  }
  .tagline {
    position: absolute;
    left: 367px;
    top: 104px;
    font-weight: 700;
    font-size: 32px;
    line-height: 39px;
  }
  .holder-name {
    position: absolute;
    right: 161px;
    top: 112px;
    font-weight: 400;
    font-size: 42px;
    line-height: 50px;
    white-space: nowrap;
  }
  .brand-name {
    position: absolute;
    left: 367px;
    top: 312px;
    font-weight: 700;
    font-size: 84px;
    line-height: 96px;
    color: var(--brand-red);
    letter-spacing: 2px;
  }
  .contact {
    position: absolute;
    top: 462px;
    font-weight: 400;
    font-size: 28px;
    line-height: 30px;
    white-space: nowrap;
  }
  .contact-phone { left: 367px; }
  .contact-address { right: 161px; text-align: right; }
</style>
</head>
<body>
  <main class="canvas">
    <div class="card"></div>
    <div class="brand-band"></div>
    <svg class="band-circle" viewBox="0 0 210 210" aria-hidden="true">
      <circle cx="105" cy="105" r="100" fill="none" stroke="#ffffff" stroke-width="6"/>
    </svg>

    <p class="tagline">Leading<br>churches<br>to the<br>Next level</p>
    <p class="holder-name">Dalen Forsythe, Dir.</p>

    <p class="brand-name">Korvanta</p>

    <p class="contact contact-phone">(555) 014-2290 Office<br>(555) 014-7736 Cell<br>dforsythe@kvmail.com</p>
    <p class="contact contact-address">2840 N. Marlow St.<br>Brenton, TX 75512<br>www.korvanta.org</p>
  </main>
</body>
</html>
```